Political sign design, fonts colors and layout

I am running for Town Council.

My message is done, and *a draft is attached* with the text we wish to use. It says "Elect Dana Velmont" etc. In Maroon and White. I am not a designer, but this is somewhat close to what we are looking for.

I need help with colors and fonts, layout, spacing, and general cleanup.

I'm attaching the town high school logo:

- "H" for Brookfield: with black and white outlines on the fonts
- we want to incorporate the black and white on the fonts
- for the entire text, parts of the text, or best would be a mix

This is for signs printed and placed all over my town.

We need two versions

1. square, 4' by 4' version
2. 36" by 24" version

The smaller version will drop the three bullet pointed text, but otherwise can be identical.

The sign can only use 3 printed colors (due to printing costs.)

1. maroon,
2. white,
3. black.

The maroon should match the maroon from the high school logo attached, which I believe I did in the draft.

We also like the white border around the outside, like in the "scoreboard" design attached.

Thanks for your attention, wish me luck.

Dana

Target Market(s)

SIgns, Political market

Industry/Entity Type

Political

Font styles to use
Sans Serif
Other font styles liked:
• Arial Black, Sans Serif Bold

Requirements
Must have
• maroon background, white font.
• - black borders around fonts where appropriate
• - great spacing
• - great typeface usage
• - clean and crisp political sign, visible while driving.
• - my name "Dana Velmont" much larger like the draft, or the appropriate additional size
• - two versions, one square, and one 36" / 24"
Nice to have
• - nice borders
• - dress it up a bit, using italics and bold fonts, without making it flashy or busy.
Should not have
• Must be easily readable from a car, except for "Paid for by Friends of Dana Velmont" which can be tiny.
• Colors are noted in the description, the "Brookfield Maroon" as the background, white font, and some use of black.

```html
<!DOCTYPE html>
<html lang="en">
<head>
<meta charset="utf-8">
<title>Elect Dana Velmont – Yard Sign</title>
<link rel="stylesheet" href="https://fonts.googleapis.com/css2?family=Bitter:ital,wght@0,800;1,700;1,800;1,900&family=Raleway:wght@600&display=swap">
<style>
  :root {
    --brookfield-maroon: #6e1230;
    --sign-white: #ffffff;
    --sign-black: #000000;
    --backdrop: #000000;
  }
  * { margin: 0; padding: 0; box-sizing: border-box; }
  html, body {
    width: 1200px; height: 1200px; overflow: hidden;
    background: var(--backdrop);
  }
  .sign {
    position: absolute; left: 100px; top: 100px;
    width: 1000px; height: 1000px;
    background: var(--brookfield-maroon);
    font-family: "Bitter", Georgia, serif;
    color: var(--sign-white);
    overflow: hidden;
  }
  .band-white { position: absolute; left: 0; width: 100%; background: var(--sign-white); }
  .band-top { top: 0; height: 106px; }
  .band-middle { top: 599px; height: 143px; }
  .swooshes { position: absolute; left: 0; top: 0; width: 1000px; height: 600px; }
  .line {
    position: absolute; left: 0; width: 100%;
    white-space: nowrap; line-height: 1;
    transform: translateY(-50%);
  }
  .centered { text-align: center; }
  .headline { top: 60px; font-size: 66px; font-weight: 800; color: var(--brookfield-maroon); letter-spacing: -1px; }
  .elect { top: 161px; left: 68px; font-size: 40px; font-style: italic; font-weight: 800; }
  .outline-heavy {
    text-shadow:
      -4px 0 0 var(--sign-black), 4px 0 0 var(--sign-black),
      0 -4px 0 var(--sign-black), 0 4px 0 var(--sign-black),
      -3px -3px 0 var(--sign-black), 3px -3px 0 var(--sign-black),
      -3px 3px 0 var(--sign-black), 3px 3px 0 var(--sign-black);
  }
  .outline-thin {
    text-shadow:
      -1.5px 0 0 var(--sign-black), 1.5px 0 0 var(--sign-black),
      0 -1.5px 0 var(--sign-black), 0 1.5px 0 var(--sign-black),
      -1px -1px 0 var(--sign-black), 1px -1px 0 var(--sign-black),
      -1px 1px 0 var(--sign-black), 1px 1px 0 var(--sign-black);
  }
  .name-first { top: 256px; left: 64px; font-size: 150px; font-style: italic; font-weight: 900; letter-spacing: -4px; }
  .name-last { top: 388px; left: auto; right: 64px; width: auto; font-size: 150px; font-style: italic; font-weight: 900; letter-spacing: -4px; }
  .for-row {
    position: absolute; top: 492px; left: 60px; width: 875px;
    display: flex; align-items: center; gap: 24px;
    transform: translateY(-50%);
  }
  .for-row .rule { flex: 1; height: 4px; background: var(--sign-white); box-shadow: 0 0 0 1px var(--sign-black); }
  .for-row .rule.short { flex: 0 0 258px; }
  .for-word { font-size: 54px; font-style: italic; font-weight: 800; line-height: 1; }
  .office { top: 553px; font-size: 58px; font-style: italic; font-weight: 800; letter-spacing: -0.5px; }
  .tagline { top: 651px; font-size: 72px; font-weight: 800; color: var(--brookfield-maroon); letter-spacing: -1.5px; }
  .website { top: 710px; font-size: 33px; font-weight: 800; color: var(--brookfield-maroon); }
  .pledge { font-size: 35px; font-weight: 800; }
  .pledge .star { font-size: 22px; vertical-align: 4px; margin: 0 6px; }
  .pledge-1 { top: 778px; }
  .pledge-2 { top: 818px; }
  .pledge-3 { top: 858px; }
  .vote { top: 922px; font-size: 82px; font-weight: 800; letter-spacing: -1.5px; }
  .disclaimer { top: 980px; font-family: "Raleway", Arial, sans-serif; font-size: 18px; font-weight: 600; }
</style>
</head>
<body>
<main class="sign">
  <div class="band-white band-top"></div>
  <svg class="swooshes" viewBox="0 0 1000 600" aria-hidden="true">
    <path fill="#ffffff" d="M380 106 Q760 128 1000 158 L1000 192 Q740 142 380 106 Z"/>
    <path fill="#ffffff" d="M300 114 Q720 150 1000 250 L1000 286 Q700 172 300 114 Z"/>
  </svg>
  <div class="band-white band-middle"></div>

  <p class="line centered headline">TAKE BACK OUR TOWN!</p>
  <p class="line elect">Elect</p>
  <h1 class="line name-first outline-heavy">DANA</h1>
  <h1 class="line name-last outline-heavy">VELMONT</h1>
  <div class="for-row"><span class="rule short"></span><span class="for-word">for</span><span class="rule"></span></div>
  <p class="line centered office outline-thin">Brookfield Councilman / Trustee</p>

  <p class="line centered tagline">FIGHTING for BROOKFIELD</p>
  <p class="line centered website">www.fairtaxbrookfield.com</p>

  <p class="line centered pledge pledge-1"><span class="star">★</span>STOP HIGH TAXES<span class="star">★</span></p>
  <p class="line centered pledge pledge-2"><span class="star">★</span>CLEAN UP OUR GOVERNMENT<span class="star">★</span></p>
  <p class="line centered pledge pledge-3"><span class="star">★</span>PRESERVE OUR NEIGHBORHOODS<span class="star">★</span></p>
  <p class="line centered vote outline-thin">Vote Nov 8th “Row A”</p>
  <p class="line centered disclaimer">Paid for by Friends of Dana Velmont</p>
</main>
</body>
</html>
```